Kelvane Plumbing Business cards

Company is Kelvane Plumbing.
name Dashel Morrowby, I am a plumber, drainer, gasfitter and roofer
Mobile: 0431 906 154
Email address: info@kelvaneplumbing.example (check out my website for some ideas)
Website: www.kelvaneplumbing.example
ABN: 82 916 203 471
LIC: 604517K

I am reliable all round plumber. I am a 24 hour emergency service. Kelvane Plumbing is a professional plumbing service in the Illawarra, South Coast, Southern Sydney and Southern Highland regions of NSW. We offer a 24 hour emergency service for piece of mind to our customers. Call us now to see how we can help you. Kelvane Plumbing approaches every job with attention to detail and excellent customer service. With our superior workmanship you can be confident that the job will be done right the first time around. You can rest assured with results that are guaranteed to last.

Target Market(s)

the general public

Contact Information for Business Card

look up website for some ideas something with similar colours to logo and new modern and to catch the eye.

Colors
fdfdfd
ffffff
000000
7f7f7f
aaaaaa
33a6d7
0492cd

Requirements
Must have
• all contact details
• company- Kelvane Plumbing
• name- Dashel Morrowby
• number mobile- 0431 906 154
• Email address- info@kelvaneplumbing.example
• Website- www.kelvaneplumbing.example
• ABN- 82 916 203 471
• LIC- 604517K

```html
<!DOCTYPE html>
<html lang="en">
<head>
<meta charset="utf-8">
<title>Kelvane Plumbing Business Cards</title>
<link href="https://fonts.googleapis.com/css2?family=Mulish:wght@300;400;700&display=swap" rel="stylesheet">
<style>
  :root {
    --page: #1c1c1c;
    --card: #000000;
    --blue: #0492cd;
    --blue-light: #33a6d7;
    --white: #ffffff;
    --grey: #7f7f7f;
    --grey-light: #aaaaaa;
    --tool-tone: rgba(90, 90, 90, 0.55);
  }
  * { margin: 0; padding: 0; box-sizing: border-box; }
  html, body {
    width: 1200px; height: 900px; overflow: hidden;
    background: var(--page);
    font-family: "Mulish", Arial, sans-serif;
  }
  .canvas { position: relative; width: 1200px; height: 900px; }
  .card {
    position: absolute; width: 700px; height: 400px;
    background: var(--card); overflow: hidden;
    box-shadow: 0 12px 30px rgba(0,0,0,.55);
  }
  .card--contact { left: 100px; top: 40px; }
  .card--front { left: 400px; top: 470px; }

  /* soft corner areas where the faint tool artwork sits */
  .corner-art {
    position: absolute; width: 170px; height: 170px;
    background: radial-gradient(circle at center, var(--tool-tone) 0%, rgba(90,90,90,0) 70%);
  }

  /* contact side */
  .brand-block {
    position: absolute; left: 0; top: 0; width: 350px; height: 400px;
    display: flex; align-items: center; justify-content: center; gap: 12px;
  }
  .brand-block__dot {
    width: 20px; height: 20px; border-radius: 50%; background: var(--blue); flex: none;
  }
  .brand-block__name {
    color: var(--blue); font-weight: 700; font-size: 28px; letter-spacing: .5px;
  }
  .divider {
    position: absolute; left: 350px; top: 60px; width: 1px; height: 280px;
    background: linear-gradient(var(--card), var(--blue-light));
  }
  .contact {
    position: absolute; left: 395px; top: 70px; color: var(--white);
  }
  .contact__name {
    color: var(--blue-light); font-size: 26px; font-weight: 400; margin-bottom: 28px;
  }
  .contact__row {
    display: flex; align-items: center; gap: 16px;
    font-size: 14px; font-weight: 300; margin-bottom: 12px;
  }
  .contact__row svg { width: 18px; height: 18px; flex: none; }
  .contact__legal {
    margin-top: 30px; font-size: 14px; font-weight: 300; line-height: 1.55;
  }

  /* front side */
  .front-content {
    position: absolute; inset: 0;
    display: flex; flex-direction: column; align-items: center; justify-content: center;
  }
  .front-brand {
    display: flex; align-items: center; gap: 14px; margin-bottom: 44px;
  }
  .front-brand__square { width: 24px; height: 24px; background: var(--blue); flex: none; }
  .front-brand__name {
    color: var(--blue); font-weight: 700; font-size: 44px; letter-spacing: 1px;
  }
  .services {
    color: var(--white); font-size: 20px; font-weight: 400;
  }
  .services .sep { color: var(--grey-light); margin: 0 10px; }
  .emergency {
    color: var(--blue-light); font-size: 24px; font-weight: 400; margin-top: 10px;
  }
</style>
</head>
<body>
<main class="canvas">

  <section class="card card--contact">
    <div class="corner-art" style="left:-70px;top:260px" role="img" aria-label="Faint tool artwork in corner"></div>
    <div class="corner-art" style="left:600px;top:-40px" role="img" aria-label="Faint tool artwork in corner"></div>

    <div class="brand-block">
      <span class="brand-block__dot"></span>
      <span class="brand-block__name">Kelvane Plumbing</span>
    </div>

    <div class="divider"></div>

    <div class="contact">
      <h1 class="contact__name">Dashel Morrowby</h1>
      <div class="contact__row">
        <svg viewBox="0 0 18 18" fill="none" stroke="#fff" stroke-width="1.4"><rect x="5" y="1.5" width="8" height="15" rx="1.5"/><line x1="8" y1="14" x2="10" y2="14"/></svg>
        <span>0431 906 154</span>
      </div>
      <div class="contact__row">
        <svg viewBox="0 0 18 18"><rect x="2" y="4" width="14" height="10" fill="#fff"/><path d="M2 4 L9 10 L16 4" fill="none" stroke="#000" stroke-width="1.2"/></svg>
        <span>info@kelvaneplumbing.example</span>
      </div>
      <div class="contact__row">
        <svg viewBox="0 0 18 18" fill="none" stroke="#fff" stroke-width="1.2"><circle cx="9" cy="9" r="7"/><ellipse cx="9" cy="9" rx="3" ry="7"/><line x1="2" y1="9" x2="16" y2="9"/></svg>
        <span>www.kelvaneplumbing.example</span>
      </div>
      <p class="contact__legal">Lic. 604517K<br>ABN: 82 916 203 471</p>
    </div>
  </section>

  <section class="card card--front">
    <div class="corner-art" style="left:-70px;top:170px" role="img" aria-label="Faint tool artwork at left edge"></div>
    <div class="corner-art" style="left:600px;top:-40px" role="img" aria-label="Faint tool artwork in corner"></div>

    <div class="front-content">
      <div class="front-brand">
        <span class="front-brand__square"></span>
        <span class="front-brand__name">Kelvane Plumbing</span>
      </div>
      <p class="services">Plumbing<span class="sep">|</span>Drainage<span class="sep">|</span>Gas Fitting<span class="sep">|</span>Roofing</p>
      <p class="emergency">24/7 Emergency Services</p>
    </div>
  </section>

</main>
</body>
</html>
```